Harbour Physiotherapy business card design

We need a fresh, new business card design for our physiotherapy clinic Harbour Physiotherapy

Will attach logo soon we had logo designed from our last project

Industry/Entity Type

Physical Therapy

Contact Information for Business Card

On front
Needs our logo, contact details:
58 Wilmot Street Glenfield NSW 2167
Ph/f: 02 9418 2753
info@harbourphysiotherapy.com.au

Requirements
Must have
• On the back of the card needs to have area to write down follow up appointments
• On front
• Needs our logo
• The colours have to be the colours in our logo which are: sky blue, black and white
• Font to be same as our logo please
• We want the card to look simple, not too cluttered but to the point
Should not have
• We don't need any extra pictures other than our logo

```html
<!DOCTYPE html>
<html lang="en">
<head>
<meta charset="utf-8">
<title>Harbour Physiotherapy – Business Card</title>
<link rel="stylesheet" href="https://fonts.googleapis.com/css2?family=Exo+2:wght@500;600;700&display=swap">
<style>
  :root {
    --sky-blue: #1169c4;
    --card-edge: #2a2a2c;
    --ink: #2e3440;
    --white: #ffffff;
    --backdrop: #ece8e2;
  }
  * { box-sizing: border-box; margin: 0; padding: 0; }
  html, body {
    width: 1108px;
    height: 1200px;
    overflow: hidden;
    background: var(--backdrop);
    font-family: "Exo 2", sans-serif;
  }
  .sheet {
    width: 1108px;
    height: 1200px;
    display: flex;
    flex-direction: column;
    align-items: center;
    justify-content: center;
    gap: 60px;
  }
  .card {
    position: relative;
    width: 900px;
    height: 514px;
    background: var(--sky-blue);
    border: 14px solid var(--card-edge);
    box-shadow: 0 10px 24px rgba(0,0,0,0.18);
    overflow: hidden;
  }

  /* Front */
  .brand {
    position: absolute;
    left: 48px;
    top: 215px;
    width: 220px;
    display: flex;
    align-items: center;
    gap: 12px;
  }
  .brand-dot {
    flex: none;
    width: 22px;
    height: 22px;
    border-radius: 50%;
    background: var(--white);
  }
  .brand-name {
    color: var(--white);
    font-weight: 600;
    font-size: 26px;
    line-height: 1.15;
  }
  .details {
    position: absolute;
    left: 320px;
    top: 120px;
  }
  .clinic-name {
    color: var(--white);
    font-weight: 600;
    font-size: 46px;
    letter-spacing: 0.5px;
    line-height: 1;
  }
  .job-title {
    color: var(--ink);
    font-weight: 600;
    font-size: 30px;
    margin-top: 10px;
  }
  .contact-list {
    list-style: none;
    margin-top: 28px;
  }
  .contact-item {
    display: flex;
    align-items: center;
    gap: 12px;
    color: var(--ink);
    font-weight: 500;
    font-size: 24px;
    margin-bottom: 12px;
  }
  .contact-icon { width: 20px; height: 20px; flex: none; }
  .contact-address { margin-top: 34px; padding-left: 32px; }

  /* Back */
  .appointment {
    position: absolute;
    left: 120px;
    top: 110px;
  }
  .appointment-heading {
    color: var(--white);
    font-weight: 700;
    font-size: 58px;
    line-height: 1;
  }
  .appointment-note {
    color: var(--ink);
    font-weight: 600;
    font-size: 24px;
    line-height: 1.25;
    margin-top: 18px;
  }
  .write-line {
    position: absolute;
    left: 120px;
    right: 80px;
    top: 360px;
    height: 12px;
    background: var(--white);
  }
</style>
</head>
<body>
<main class="sheet">
  <section class="card card-front" aria-label="Card front">
    <div class="brand">
      <span class="brand-dot"></span>
      <span class="brand-name">Harbour Physiotherapy</span>
    </div>
    <div class="details">
      <h1 class="clinic-name">physiotherapy clinic</h1>
      <p class="job-title">Title</p>
      <ul class="contact-list">
        <li class="contact-item">
          <svg class="contact-icon" viewBox="0 0 24 24" aria-hidden="true"><path fill="#ffffff" d="M6.6 10.8a15 15 0 0 0 6.6 6.6l2.2-2.2c.3-.3.7-.4 1-.2 1.1.4 2.3.6 3.6.6.6 0 1 .4 1 1V20c0 .6-.4 1-1 1A17 17 0 0 1 3 4c0-.6.4-1 1-1h3.5c.6 0 1 .4 1 1 0 1.3.2 2.5.6 3.6.1.3 0 .7-.2 1z"/></svg>
          <span>02 9418 2753</span>
        </li>
        <li class="contact-item">
          <svg class="contact-icon" viewBox="0 0 24 24" aria-hidden="true"><rect x="2" y="5" width="20" height="14" rx="1.5" fill="#ffffff"/><path d="M3 6l9 7 9-7" fill="none" stroke="#1169c4" stroke-width="1.8"/></svg>
          <span>info@harbourphysiotherapy.com.au</span>
        </li>
        <li class="contact-item contact-address">58 Wilmot Street Glenfield NSW 2167</li>
      </ul>
    </div>
  </section>

  <section class="card card-back" aria-label="Card back">
    <div class="appointment">
      <h2 class="appointment-heading">Appoinment</h2>
      <p class="appointment-note">If you anable keep your Appoinment,<br>please contect us As soon As possible</p>
    </div>
    <div class="write-line"></div>
  </section>
</main>
</body>
</html>
```